Brochure Design- Targeted at Property Developers

We are the largest Conveyancing (property law) firm in the state of Victoria, Australia.

We need a very sophisticated brochure to enable us to take the next step and compete with law firms for property developer clients.

Much about us can be found on our website (inlcuding logos, photos, etc) www.trellowby.com.au but our business name is Trellowby- Marsh Vale not just Trellowby. ALSO I HAVE ATTACHED MANY PHOTOS OF OUR STAFF AND SOME LOGOS TO HELP!!

Size: fold (A3 double sided so that there is 4 A4 pages)

Copy:

This can be played with by the designer to spread across the 4 pages. Ideally the front page will be very minimalistic and not mention our brand (or at least the brand should not dominate):

Page 1: Do property developers have a genuine alternative to high legal fees?

Page 2 and 3:

- 100% of our developer clients recommend us
- We already look after the Conveyancing needs of more developers in Victoria than any other Conveyancing firm
- Industry benchmark off- the- plan contracts (tailored to the requirements of each development). Our special conditions (including variations, rebates and resale restrictions) are carefully chosen to protect the interests of our vendors while being commercially sensitive to ensure sales are not lost unnecessarily
- Expert in guiding developers from first time dual occupancies to seasoned developers of large scale land and highrise projects
- Our large team and highly refined systems ensure fastest possible settlement times after subdivision registration
- We are available to train your project marketers on completing and executing contracts so that sales are not delayed or lost
- Establishment of interest bearing trust accounts
- Before you buy a development site have us thoroughly investigate the contract and vendors statement. We can then conduct the purchase settlement on your behalf.
- We have the friendliest and most efficient staff. Every dealing you have with our dedicated Development Division will be prompt, professional and impressive. You will never need to follow us up!
- Highly experienced Conveyancers with the security of full Solicitor support

Please consider us next time you need Conveyancing.

Services options:
- Use us from contract preparation to settlement or;
- Have your Solicitor prepare the contract and use us as an alternative for the settlement stage only. Many Solicitors recommend us for this service already
- Fast subdivision lodgements (including obtaining mortgagee’s consent, Solicitor preparation of Land Titles Office application, owners corporation establishment)

Page 4: Just our contact details (see our website)

The design should make us look highly professional, conservative, yet cutting edge.

Target Market(s)

Property developers of small to medium sized land and unit developments

Industry/Entity Type

Security

Requirements
Must have
• - Our logo and contact details as well as the copy above.
Nice to have
• - Pictures of land sites, highrise buildings under construction
Should not have
• I really dislike overly corny photos where everyone is fake and smiling. Other photos would be great but not too cheesy.

```html
<!DOCTYPE html>
<html lang="en">
<head>
<meta charset="utf-8">
<title>Trellowby Marsh Vale – Developer Brochure</title>
<link rel="stylesheet" href="https://fonts.googleapis.com/css2?family=Lato:wght@400;700&family=Jost:wght@500&family=Nunito:wght@800&family=Varela+Round&display=swap">
<style>
  :root {
    --navy: #2e2c6c;
    --navy-deep: #26245e;
    --lilac: #a9a6cc;
    --white: #ffffff;
    --ink: #1a1a1a;
    --yellow: #f4ee2c;
    --yellow-pale: #fbf9c8;
    --shadow: rgba(0,0,0,0.35);
  }
  * { box-sizing: border-box; margin: 0; padding: 0; }
  html, body { width: 1200px; height: 900px; overflow: hidden; background: var(--white); }
  body { position: relative; font-family: "Lato", sans-serif; }

  .spread { position: absolute; box-shadow: 2px 3px 6px var(--shadow); border: 1px solid #222; overflow: hidden; }

  /* Inner spread */
  .spread--inner { left: 510px; top: 405px; width: 672px; height: 475px; background: var(--white); }
  .inner-right {
    position: absolute; left: 316px; top: 0; width: 356px; height: 475px;
    background: linear-gradient(180deg, var(--navy) 0%, var(--navy) 35%, #7874a8 70%, var(--white) 100%);
  }
  .photo { position: absolute; }
  .photo--cranes { left: 0; top: 0; width: 149px; height: 115px; background: linear-gradient(160deg, #4f86b8 0%, #9cc0dc 45%, #c9b48a 80%, #a9773f 100%); }
  .photo--city { left: 152px; top: 0; width: 204px; height: 115px; background: linear-gradient(180deg, #2f3b5e 0%, #56607e 45%, #b27a48 75%, #6b7486 100%); }

  .services {
    position: absolute; left: 67px; top: 125px; width: 264px; height: 160px;
    background: var(--white); border-radius: 14px;
    box-shadow: 0 0 10px 6px rgba(255,255,255,0.7);
    padding: 10px 12px; font-size: 7.4px; line-height: 1.35; color: var(--ink);
  }
  .services p { margin-bottom: 6px; }
  .services ul { list-style: none; }
  .services li { position: relative; padding-left: 10px; margin-bottom: 6px; }
  .services li::before { content: ">"; position: absolute; left: 0; }
  .services .brand-box { position: absolute; left: 47px; top: 127px; width: 138px; height: 60px; font-size: 15px; }

  .brand-box {
    background: var(--navy-deep); color: var(--white);
    display: flex; align-items: center; justify-content: center; text-align: center;
    font-family: "Lato", sans-serif; font-weight: 400; line-height: 1.05;
  }

  .team-line {
    position: absolute; left: 0; width: 356px; top: 329px; text-align: center;
    font-family: "Varela Round", sans-serif; font-size: 12.5px; font-style: italic; color: var(--white);
  }
  .portrait { position: absolute; top: 357px; width: 87px; height: 118px; }
  .portrait--1 { left: 36px; background: linear-gradient(180deg, #e2e2e2 0%, #b99a86 35%, #6e5546 60%, #1e1e1e 100%); }
  .portrait--2 { left: 140px; background: linear-gradient(180deg, #1e1e1e 0%, #3a2f2a 25%, #c8a898 50%, #232323 80%, #111 100%); }
  .portrait--3 { left: 248px; background: linear-gradient(180deg, #dcdcdc 0%, #c29a84 40%, #8a6a58 60%, #262626 100%); }

  /* Yellow benefits panel */
  .benefits {
    position: absolute; left: 545px; top: 568px; width: 265px; height: 325px;
    transform: rotate(-2.6deg); transform-origin: top left;
    background: linear-gradient(180deg, var(--yellow) 0%, var(--yellow) 40%, var(--yellow-pale) 100%);
    box-shadow: 2px 3px 6px var(--shadow);
    padding: 26px 12px 0 14px;
    font-family: "Jost", sans-serif; font-weight: 500; font-size: 7.6px; line-height: 1.45; color: var(--ink);
  }
  .benefits ul { list-style: none; }
  .benefits li { position: relative; padding-left: 10px; margin-bottom: 8px; }
  .benefits li::before { content: ">"; position: absolute; left: 0; }

  /* Outer spread */
  .spread--outer { left: 14px; top: 14px; width: 812px; height: 576px; display: flex; }
  .back-page {
    position: relative; width: 406px; height: 100%;
    background: linear-gradient(180deg, var(--navy) 0%, #45427c 35%, var(--lilac) 70%, var(--white) 90%);
  }
  .contact {
    position: absolute; left: 0; top: 141px; width: 406px; text-align: center;
    color: var(--white); font-size: 10.6px; line-height: 13.2px; font-style: normal;
  }
  .back-page .brand-box { position: absolute; left: 133px; top: 306px; width: 134px; height: 60px; font-size: 15px; }
  .map {
    position: absolute; left: 64px; top: 386px; width: 277px; height: 190px;
    border-radius: 22px 22px 0 0;
    background: linear-gradient(135deg, #f3eef0 0%, #e2dde2 40%, #c9c6cc 55%, #ece7ea 70%, #e6dfe2 100%);
  }
  .cover {
    position: relative; width: 406px; height: 100%;
    background: linear-gradient(180deg, #161c3a 0%, #2d5a9a 35%, #5b93c8 60%, #b9b8b4 85%, #c98a45 100%);
  }
  .headline {
    position: absolute; right: 20px; top: 76px; text-align: right;
    font-family: "Nunito", sans-serif; font-weight: 800; color: var(--white);
    font-size: 24px; line-height: 36px; letter-spacing: 0.3px;
    text-shadow: 0 0 6px #3a4fa0, 0 0 12px #2b3a88;
  }
  .headline .big { font-size: 29px; }
  .cover .brand-box { position: absolute; left: 222px; top: 458px; width: 164px; height: 73px; font-size: 18px; }
</style>
</head>
<body>

  <section class="spread spread--inner" aria-label="Inside spread">
    <div class="inner-right">
      <div class="photo photo--cranes" role="img" aria-label="Photo of tower cranes over a building site"></div>
      <div class="photo photo--city" role="img" aria-label="Photo of a city skyline and river at dusk"></div>

      <div class="services">
        <p>Please consider us next time you need Conveyancing.</p>
        <p>Services options:</p>
        <ul>
          <li>Use us from contract preparation to settlement or;</li>
          <li>Have your Solicitor prepare the contract and use us as an alternative for the settlement stage only. Many Solicitors recommend us for this service already</li>
          <li>Fast subdivision lodgements (including obtaining mortgagee’s consent, Solicitor preparation of Land Titles Office application, owners corporation establishment)</li>
        </ul>
        <div class="brand-box">Trellowby<br>Marsh Vale</div>
      </div>

      <p class="team-line">Our team of friendly staff are ready to help you...</p>
      <div class="portrait portrait--1" role="img" aria-label="Portrait photo of a staff member"></div>
      <div class="portrait portrait--2" role="img" aria-label="Portrait photo of a staff member"></div>
      <div class="portrait portrait--3" role="img" aria-label="Portrait photo of a staff member"></div>
    </div>
  </section>

  <aside class="benefits" aria-label="Why developers choose us">
    <ul>
      <li>Industry benchmark off-the-plan contracts (tailored to the requirements of each development). Our special conditions (including variations, rebates and resale restrictions) are carefully chosen to protect the interests of our vendors while being commercially sensitive to ensure sales are not lost unnecessarily</li>
      <li>Expert in guiding developers from first time dual occupancies to seasoned developers of large scale land and highrise projects</li>
      <li>Our large team and highly refined systems ensure fastest possible settlement times after subdivision registration</li>
      <li>We are available to train your project marketers on completing and executing contracts so that sales are not delayed or lost</li>
      <li>Establishment of interest bearing trust accounts</li>
      <li>Before you buy a development site have us thoroughly investigate the contract and vendors statement. We can then conduct the purchase settlement on your behalf.</li>
      <li>We have the friendliest and most efficient staff. Every dealing you have with our dedicated Development Division will be prompt, professional and impressive. You will never need to follow us up!</li>
      <li>Highly experienced Conveyancers with the security of full Solicitor support</li>
    </ul>
  </aside>

  <section class="spread spread--outer" aria-label="Outside spread">
    <div class="back-page">
      <address class="contact">
        Address: Level 7, 12 Harlow Crescent<br>
        Marsh Vale 3104 Victoria<br>
        Australia<br>
        (Off Kestrel Road)<br>
        Postal: PO Box 4410 Kestrel Road Central Marsh Vale 8108<br>
        DX Postal: DX 40817 South Marsh Vale<br>
        Phone: (03) 9000 4120<br>
        International: +61 3 9000 4120<br>
        Fax: (03) 9000 4121<br>
        International Fax: +61 3 9000 4121<br>
        Email: enquiries@trellowby.com.au
      </address>
      <div class="brand-box">Trellowby<br>Marsh Vale</div>
      <div class="map" role="img" aria-label="Street map showing the office location off Kestrel Road"></div>
    </div>
    <div class="cover" role="img" aria-label="Photo of tower cranes silhouetted against a dusk sky">
      <h1 class="headline">Do property<br>developers have a<br>genuine <span class="big">alternative</span><br>to <span class="big">high legal fees?</span></h1>
      <div class="brand-box">Trellowby<br>Marsh Vale</div>
    </div>
  </section>

</body>
</html>
```